Cd Cover design for Chicago based record label.

Cd Cover design for a new single! Song is dedicated to exotic dancers. We do not want our artist pictures on this one. So please use your imagination. Song Title: "Slow Burnout". Thanks? Artist: Lenny Sparrows feat. Kid Tango.

```html
<!DOCTYPE html>
<html lang="en">
<head>
<meta charset="utf-8">
<title>Slow Burnout – Lenny Sparrows feat. Kid Tango</title>
<link href="https://fonts.googleapis.com/css2?family=Advent+Pro:wght@200;300&family=Courier+Prime:wght@400;700&display=swap" rel="stylesheet">
<style>
  :root {
    --stage: #222a2d;
    --cover-dark: #141414;
    --cover-mid: #262626;
    --title-grey: #b3b3b3;
    --pole-grey: #a6a6a6;
    --artist-white: #ffffff;
    --accent-lime: #c9c82c;
  }
  * { margin: 0; padding: 0; box-sizing: border-box; }
  html, body {
    width: 1200px;
    height: 799px;
    overflow: hidden;
    background: var(--stage);
  }
  .cover {
    position: absolute;
    left: 270px;
    top: 71px;
    width: 658px;
    height: 658px;
    background: linear-gradient(160deg, var(--cover-mid) 0%, var(--cover-dark) 70%);
    overflow: hidden;
  }
  .song-title {
    position: absolute;
    right: 378px;
    top: 124px;
    font-family: "Advent Pro", "Arial Narrow", sans-serif;
    font-weight: 200;
    color: var(--title-grey);
    text-align: right;
    text-transform: uppercase;
    line-height: 114px;
    font-size: 146px;
    letter-spacing: -2px;
    transform: scaleX(0.8);
    transform-origin: right top;
  }
  .song-title .title-line { display: block; }
  .credits {
    position: absolute;
    right: 379px;
    top: 488px;
    text-align: right;
    font-family: "Courier Prime", "Courier New", monospace;
  }
  .artist-name {
    color: var(--artist-white);
    font-size: 24px;
    font-weight: 700;
    line-height: 28px;
  }
  .featured-artist {
    color: var(--accent-lime);
    font-size: 16px;
    font-weight: 700;
    line-height: 22px;
  }
  .pole {
    position: absolute;
    left: 332px;
    top: 89px;
    width: 9px;
    height: 479px;
    background: var(--pole-grey);
  }
  .dancer-art {
    position: absolute;
    left: 352px;
    top: 127px;
    width: 276px;
    height: 370px;
  }
</style>
</head>
<body>
  <main class="cover">
    <h1 class="song-title">
      <span class="title-line">Slow</span>
      <span class="title-line">Burn</span>
      <span class="title-line">out</span>
    </h1>
    <div class="credits">
      <p class="artist-name">Lenny Sparrows</p>
      <p class="featured-artist">feat. Kid Tango</p>
    </div>
    <div class="pole"></div>
    <svg class="dancer-art" viewBox="0 0 276 370" role="img" aria-label="Silhouette illustration of a pole dancer in a split pose, white figure with lime heels, briefs and ponytail">
      <defs>
        <radialGradient id="dancer-glow" cx="50%" cy="50%" r="50%">
          <stop offset="0%" stop-color="#ffffff" stop-opacity="0.85"/>
          <stop offset="55%" stop-color="#e6e5b4" stop-opacity="0.45"/>
          <stop offset="100%" stop-color="#c9c82c" stop-opacity="0"/>
        </radialGradient>
      </defs>
      <rect x="0" y="0" width="276" height="370" fill="url(#dancer-glow)"/>
    </svg>
  </main>
</body>
</html>
```